Leadership Brenvale Brochure Design*

We host a local leadership development program every two years. We need a brochure to promote the program. We would like it to be 8 1/2 x 11, tri-fold. I have attached a Word document with the necessary info for the brochure. The brochure will be professionally printed. We would like the final design to be in InDesign.

Target Market(s)

Potential participants of our leadership program. They will be local leaders, male and female, from 30-60 years of age.

Requirements
Must have
• Content as detailed in the Word document attached. Our logo.
Nice to have
• A design that is attractive to young professionals.

```html
<!DOCTYPE html>
<html lang="en">
<head>
<meta charset="utf-8">
<title>Leadership Brenvale – Program Brochure</title>
<link href="https://fonts.googleapis.com/css2?family=Open+Sans:wght@400;600;700&display=swap" rel="stylesheet">
<style>
:root{
  --backdrop:#c4c5c7;
  --paper:#ffffff;
  --blue:#0b4fa4;
  --orange:#f2801f;
  --card:#dedfe2;
  --ink:#1c1c1c;
  --heading-blue:#1e8ad6;
  --navy:#1a2d7a;
}
*{box-sizing:border-box;margin:0;padding:0}
html,body{width:1200px;height:1000px;overflow:hidden}
body{background:var(--backdrop);font-family:"Open Sans",Arial,sans-serif;color:var(--ink);position:relative}
.brochure{position:absolute;left:80px;top:90px;width:1040px;height:803px;background:var(--paper);overflow:hidden}
.panel{position:absolute;top:0;height:803px;width:347px}
.panel-1{left:0}.panel-2{left:347px}.panel-3{left:694px;width:346px}

.band{position:absolute;left:0;width:100%;z-index:2}
.band-blue{background:var(--blue)}
.band-orange{background:var(--orange)}

.overview-title{position:absolute;left:46px;top:32px;display:flex;align-items:center;gap:16px;color:#fff;font-weight:700;font-size:16px;z-index:3}
.round-icon{width:33px;height:33px;border-radius:50%;background:#fff;display:flex;align-items:center;justify-content:center}

.intro{position:absolute;left:46px;top:81px;width:282px;font-size:10.6px;line-height:18.4px}
.goals{position:absolute;left:46px;top:240px;width:282px;list-style:none}
.goals li{display:flex;gap:17px;font-size:10.6px;line-height:18.2px;margin-bottom:4px}
.goals .box{flex:none;width:23px;height:23px;background:var(--orange);position:relative;margin-top:4px}
.goals .box::after{content:"";position:absolute;left:8px;top:3px;width:5px;height:11px;border:solid #fff;border-width:0 2.5px 2.5px 0;transform:rotate(40deg)}

.schedule-tag{position:absolute;left:46px;top:397px;width:142px;height:25px;background:var(--blue);color:#fff;font-weight:700;font-size:16px;display:flex;align-items:center;gap:8px;padding-left:22px}

.card{position:absolute;background:var(--card);padding:17px 13px 0 13px}
.card-time{position:absolute;left:13px;top:-13px;width:168px;height:25px;background:var(--blue);color:#fff;font-size:10.8px;display:flex;align-items:center;gap:8px;padding-left:14px;white-space:nowrap}
.card-date{position:absolute;left:187px;top:-13px;width:71px;height:25px;background:var(--orange);color:#fff;font-size:10.8px;display:flex;align-items:center;padding-left:8px;white-space:nowrap}
.clock{width:21px;height:21px;border-radius:50%;background:#fff;display:flex;align-items:center;justify-content:center}
.card-title{font-weight:700;font-size:10.8px;line-height:16px;margin-bottom:10px}
.agenda{list-style:none}
.agenda li{position:relative;padding-left:20px;font-size:10.6px;line-height:18.4px}
.agenda li::before{content:"";position:absolute;left:4px;top:3px;width:5px;height:10px;border:solid var(--ink);border-width:0 2.5px 2.5px 0;transform:rotate(40deg)}
.agenda.light li{padding-left:22px}
.agenda.light li::before{border-color:#fff}

.info{position:absolute;left:25px;width:285px;font-size:10.6px;line-height:18.3px}
.info h2{color:var(--heading-blue);font-size:12.4px;font-weight:700;margin-bottom:1px}
.contact{position:absolute;left:27px;top:697px;font-size:10.6px}
.phone{display:flex;align-items:center;gap:6px;color:var(--navy);font-weight:700;font-size:13px;margin-top:2px}
</style>
</head>
<body>
<div class="brochure">

  <section class="panel panel-1">
    <div class="band band-blue" style="top:0;height:70px"></div>
    <h1 class="overview-title">
      <span class="round-icon">
        <svg width="20" height="20" viewBox="0 0 20 20" fill="#0b4fa4"><circle cx="10" cy="4" r="3"/><rect x="6.5" y="7.5" width="7" height="3" rx="1.5"/><circle cx="4.5" cy="12.5" r="2.5"/><circle cx="15.5" cy="12.5" r="2.5"/><rect x="1.5" y="15.3" width="6" height="3" rx="1.5"/><rect x="12.5" y="15.3" width="6" height="3" rx="1.5"/></svg>
      </span>
      Program Overview
    </h1>
    <p class="intro">Leadership Brenvale is a leadership certification program designed to prepare the leaders of tomorrow. During the five-month program, participants get an in-depth view of community issues, develop leadership skills necessary to assume leadership roles, and are exposed to community involvement opportunities. Leadership Brenvale will provide participants with the opportunities to:</p>
    <ul class="goals">
      <li><span class="box"></span><span>Build and demonstrate leadership and communication skills</span></li>
      <li><span class="box"></span><span>Think critically about key business, policy, and civic issues facing Brenvale County</span></li>
      <li><span class="box"></span><span>Build meaningful, long-lasting connections</span></li>
      <li><span class="box"></span><span>Establish ongoing dialogues with experienced community leaders</span></li>
    </ul>
    <div class="schedule-tag">
      <svg width="19" height="19" viewBox="0 0 19 19"><rect x="1" y="3" width="15" height="14" rx="1.5" fill="#f2801f"/><rect x="1" y="3" width="15" height="4" fill="#fff" opacity=".5"/><circle cx="13.5" cy="13.5" r="4.5" fill="#fff"/><path d="M13.5 11v3h2" stroke="#f2801f" stroke-width="1.4" fill="none"/></svg>
      Schedule:
    </div>

    <div class="card" style="left:46px;top:441px;width:274px;height:167px">
      <div class="card-time"><span class="clock"><svg width="15" height="15" viewBox="0 0 15 15"><circle cx="7.5" cy="7.5" r="6" fill="none" stroke="#0b4fa4" stroke-width="1.6"/><path d="M7.5 4v4h3" stroke="#0b4fa4" stroke-width="1.6" fill="none"/></svg></span>10:00 a.m. – 7:00 p.m.</div>
      <div class="card-date">January 17</div>
      <h3 class="card-title">Organizational Retreat &amp; Dinner<br>(Attendance Mandatory)</h3>
      <ul class="agenda"><li>Introductions</li><li>Team Building</li><li>Motivation</li><li>Leadership Styles</li><li>Social Hour/Dinner</li></ul>
    </div>

    <div class="card" style="left:46px;top:630px;width:274px;height:128px">
      <div class="card-time"><span class="clock"><svg width="15" height="15" viewBox="0 0 15 15"><circle cx="7.5" cy="7.5" r="6" fill="none" stroke="#0b4fa4" stroke-width="1.6"/><path d="M7.5 4v4h3" stroke="#0b4fa4" stroke-width="1.6" fill="none"/></svg></span>8:30 a.m. – 4:00 p.m</div>
      <div class="card-date">January 31</div>
      <h3 class="card-title">Business &amp; Industry</h3>
      <ul class="agenda"><li>Business &amp; Industry Panel</li><li>Tour of Ironleaf Manufacturing facility</li><li>Tour of Harlow Tool Company</li><li>“Taking your vision into B&amp;I”</li></ul>
    </div>

    <div class="band band-orange" style="top:758px;height:45px"></div>
  </section>

  <section class="panel panel-2">
    <div class="band band-orange" style="top:0;height:35px"></div>
    <div class="band band-blue" style="top:35px;height:35px"></div>

    <div class="card" style="left:36px;top:103px;width:273px;height:161px">
      <div class="card-time"><span class="clock"><svg width="15" height="15" viewBox="0 0 15 15"><circle cx="7.5" cy="7.5" r="6" fill="none" stroke="#0b4fa4" stroke-width="1.6"/><path d="M7.5 4v4h3" stroke="#0b4fa4" stroke-width="1.6" fill="none"/></svg></span>8:30 a.m. – 4:00 p.m</div>
      <div class="card-date">February 21</div>
      <h3 class="card-title">Education</h3>
      <ul class="agenda"><li>Tour of selected programs at BCC</li><li>College Career Program overview</li><li>Lunch at Brenvale Career and College Academy</li><li>Tour of BCCA</li><li>Overview of CTE program paths</li></ul>
    </div>

    <div class="card" style="left:36px;top:290px;width:273px;height:125px">
      <div class="card-time"><span class="clock"><svg width="15" height="15" viewBox="0 0 15 15"><circle cx="7.5" cy="7.5" r="6" fill="none" stroke="#0b4fa4" stroke-width="1.6"/><path d="M7.5 4v4h3" stroke="#0b4fa4" stroke-width="1.6" fill="none"/></svg></span>8:30 a.m. – 4:00 p.m</div>
      <div class="card-date">March 14</div>
      <h3 class="card-title">Future Technologies &amp;<br>Communications</h3>
      <ul class="agenda"><li>BCC Presents interview</li><li>Trends and forecasts</li><li>Marketing &amp; communications panel</li></ul>
    </div>

    <div class="card" style="left:36px;top:440px;width:273px;height:142px">
      <div class="card-time"><span class="clock"><svg width="15" height="15" viewBox="0 0 15 15"><circle cx="7.5" cy="7.5" r="6" fill="none" stroke="#0b4fa4" stroke-width="1.6"/><path d="M7.5 4v4h3" stroke="#0b4fa4" stroke-width="1.6" fill="none"/></svg></span>8:30 a.m. – 4:00 p.m</div>
      <div class="card-date">April 4</div>
      <h3 class="card-title">Government</h3>
      <ul class="agenda"><li>Overview of state/federal government</li><li>Overview of city/county government</li><li>Tour of Ashford Correctional Institute</li><li>Tour of courthouse</li><li>Judicial presentations</li></ul>
    </div>

    <div class="card" style="left:36px;top:612px;width:273px;height:146px">
      <div class="card-time"><span class="clock"><svg width="15" height="15" viewBox="0 0 15 15"><circle cx="7.5" cy="7.5" r="6" fill="none" stroke="#0b4fa4" stroke-width="1.6"/><path d="M7.5 4v4h3" stroke="#0b4fa4" stroke-width="1.6" fill="none"/></svg></span>8:30 a.m. – 4:00 p.m</div>
      <div class="card-date">May2</div>
      <h3 class="card-title">Health &amp; Wellness</h3>
      <ul class="agenda"><li>Tour of Riverbend Hospice</li><li>Community Wellness Roundtable</li><li>Tour of Maplewood Cancer Care Center</li><li>Virtual Medicine Tutorial</li><li>Tour of BRHS</li></ul>
    </div>

    <div class="band band-orange" style="top:758px;height:45px"></div>
  </section>

  <section class="panel panel-3">
    <div class="band band-orange" style="top:0;height:35px"></div>
    <div class="band band-blue" style="top:35px;height:35px"></div>

    <div class="card" style="left:25px;top:103px;width:273px;height:120px">
      <div class="card-time"><span class="clock"><svg width="15" height="15" viewBox="0 0 15 15"><circle cx="7.5" cy="7.5" r="6" fill="none" stroke="#0b4fa4" stroke-width="1.6"/><path d="M7.5 4v4h3" stroke="#0b4fa4" stroke-width="1.6" fill="none"/></svg></span>12:00 p.m.</div>
      <div class="card-date">May 18</div>
      <h3 class="card-title">Graduation Ceremony and<br>Luncheon</h3>
      <ul class="agenda light"><li>Participants are encouraged to invite their employer/supervisor/mentor/special guest (x2)</li></ul>
    </div>

    <div class="info" style="top:238px">
      <h2>Attendance Policy</h2>
      <p>Attendance at all sessions including the opening retreat is compulsory.&nbsp; Participants may miss no more than one session to graduate; however, the Organizational Retreat is mandatory.</p>
    </div>
    <div class="info" style="top:348px">
      <h2>Tuition</h2>
      <p>If accepted in the Leadership Brenvale program, you or your employer/sponsor will be invoiced $400 for Chamber members and $500 for non-members.&nbsp; This fee covers costs for the retreat, classroom sessions, lunches, and graduation.&nbsp; No refunds will be provided for participants who drop out of the program or do not fulfill the required curriculum.</p>
    </div>
    <div class="info" style="top:514px">
      <h2>To Apply</h2>
      <p>Applications are available on the Chamber’s website, www.TheBrenvaleChamber.com Applications are due by November 2, 2020.<br>Class size is limited.&nbsp; All applications received by the deadline will be reviewed and final participants for the Leadership Brenvale class will be contacted on December 4, 2020.&nbsp; However, all applicants will be notified of the status of their application in writing.</p>
    </div>
    <div class="contact">
      <p>For questions, please call the Chamber</p>
      <p class="phone">
        <svg width="15" height="15" viewBox="0 0 15 15"><circle cx="7.5" cy="7.5" r="6.5" fill="none" stroke="#1a2d7a" stroke-width="1.3"/><path d="M5 4.2l1.3-.3.8 1.8-.9.7c.4.9 1 1.5 1.9 1.9l.7-.9 1.8.8-.3 1.3c-2.8 0-5.3-2.5-5.3-5.3z" fill="#1a2d7a"/></svg>
        555-014-2286
      </p>
    </div>

    <div class="band band-blue" style="top:758px;height:45px"></div>
  </section>

</div>
</body>
</html>
```